Postcard Design

Tavimelon Frozen Yogurt -- small frozen yogurt/soft serve shop inside Pinecrest Plaza. We also have cookies, smoothies and coffee. Frozen Yogurt is self-serve with topping bar and priced by weight. We're locally owned and our cookies and yogurt are all hand made at the store.

We'd like to create a postcard containing 3 or 4 coupons for distribution via direct mail, inclusion in event participant gift bags, etc.

Design-wise, our logo and store feature bright colors (lime green, fuscia, dark purple, orange...) but I'd like to quiet down the overall look of the piece with possibly a brown paper bag and bright accents feel. I'd like the look of the piece to suggest a healthy, quality product.

coupon options: Buy one get one free (equal or lesser value) // save $1 // free waffle cone with froyo purchase // 50% off smoothie

```html
<!DOCTYPE html>
<html lang="en">
<head>
<meta charset="utf-8">
<title>Tavimelon Frozen Yogurt – Coupon Postcard</title>
<link rel="stylesheet" href="https://fonts.googleapis.com/css2?family=Teko:wght@500;600&family=Tinos&display=swap">
<style>
  :root {
    --backdrop: #2b2b2d;
    --pink-deep: #ff86c0;
    --pink-light: #fdb6d8;
    --pink-mid: #fa9ccb;
    --accent-pink: #e0137a;
    --purple: #6a3f8c;
    --ink: #1d1a17;
    --gold-dark: #c9a228;
    --gold-light: #f4dc73;
    --white: #ffffff;
    --line-grey: #9a9a9a;
  }
  * { box-sizing: border-box; margin: 0; padding: 0; }
  html, body { width: 900px; height: 1200px; overflow: hidden; }
  body { background: var(--backdrop); position: relative; font-family: "Tinos", serif; }

  .postcard {
    position: absolute;
    box-shadow: 0 6px 18px rgba(0,0,0,0.45);
    overflow: hidden;
  }

  /* ---------- Front ---------- */
  .postcard--front {
    left: 143px; top: 70px; width: 637px; height: 488px;
    background: linear-gradient(90deg, var(--pink-deep) 0%, var(--pink-light) 62%, var(--pink-mid) 100%);
  }
  .sundae-art {
    position: absolute; left: 14px; top: 16px; width: 252px; height: 456px;
    border-radius: 120px 120px 60px 60px;
    background: radial-gradient(ellipse at 50% 35%, #f7a9cf 0%, #f3c6dc 45%, #e8eef0 80%);
    border: 8px solid var(--white);
  }
  .store-id {
    position: absolute; left: 312px; top: 0; width: 300px; height: 100%;
    text-align: center;
  }
  .store-id > * { position: absolute; left: 0; width: 100%; }
  .brand-mark {
    top: 112px; left: 80px; width: 140px; height: 140px;
    border-radius: 50%; background: var(--purple);
  }
  .brand-name {
    top: 282px;
    font-family: "Tinos", serif; font-size: 29px; line-height: 1;
    color: var(--purple); white-space: nowrap;
  }
  .store-location { top: 360px; font-size: 24px; line-height: 1; color: var(--white); }
  .store-address { top: 396px; font-size: 17px; line-height: 23px; color: var(--ink); }
  .store-phone { top: 446px; font-size: 16px; line-height: 1; color: var(--ink); }

  /* ---------- Back ---------- */
  .postcard--back {
    left: 145px; top: 645px; width: 633px; height: 490px;
    background: var(--white);
  }
  .coupon-panel {
    position: absolute; left: 0; top: 0; width: 435px; height: 100%;
    background: linear-gradient(90deg, var(--pink-mid) 0%, var(--pink-light) 55%, var(--pink-deep) 100%);
  }
  .coupon {
    position: absolute; left: 87px; width: 246px; height: 95px;
    border-radius: 14px;
    border: 1.5px dashed #3a3124;
    background: linear-gradient(90deg, var(--gold-dark) 0%, var(--gold-light) 50%, var(--gold-dark) 100%);
    display: flex; flex-direction: column; align-items: center; justify-content: center;
    font-family: "Teko", sans-serif; font-weight: 500; color: var(--ink);
    text-transform: uppercase; line-height: 0.9;
  }
  .coupon--bogo { top: 32px; }
  .coupon--save { top: 139px; flex-direction: row; gap: 8px; }
  .coupon--cone { top: 250px; }
  .coupon--smoothie { top: 365px; flex-direction: row; gap: 6px; }

  .coupon__headline { font-size: 30px; }
  .coupon__condition { font-size: 19px; color: var(--accent-pink); margin-top: 4px; }
  .coupon__amount { font-size: 68px; color: var(--accent-pink); font-weight: 600; }
  .coupon__save-word { font-size: 40px; }
  .coupon__stack { font-size: 27px; line-height: 0.85; text-align: left; }

  .scissors { position: absolute; width: 26px; height: 18px; }

  .stamp-box {
    position: absolute; left: 510px; top: 31px; width: 94px; height: 106px;
    border: 1.5px solid #333;
  }
  .address-line {
    position: absolute; left: 455px; width: 155px; height: 1px; background: var(--line-grey);
  }
  .back-brand {
    position: absolute; left: 455px; top: 425px; width: 160px;
    display: flex; align-items: center; justify-content: center; gap: 6px;
    font-family: "Tinos", serif; font-size: 20px; color: var(--purple);
  }
  .back-brand .dot { width: 10px; height: 10px; border-radius: 50%; background: var(--purple); flex: none; }
</style>
</head>
<body>
  <svg width="0" height="0" style="position:absolute">
    <symbol id="icon-scissors" viewBox="0 0 26 18">
      <circle cx="5" cy="4" r="3.2" fill="none" stroke="#1d1a17" stroke-width="1.6"/>
      <circle cx="5" cy="14" r="3.2" fill="none" stroke="#1d1a17" stroke-width="1.6"/>
      <path d="M7.5 5.5 L25 14 M7.5 12.5 L25 4" stroke="#1d1a17" stroke-width="1.6" stroke-linecap="round"/>
    </symbol>
  </svg>

  <section class="postcard postcard--front">
    <div class="sundae-art" role="img" aria-label="Illustration of a pink frozen yogurt sundae in a glass cup with chocolate sauce, a strawberry and wafer rolls"></div>
    <div class="store-id">
      <span class="brand-mark"></span>
      <p class="brand-name">Tavimelon Frozen Yogurt</p>
      <p class="store-location">Pinecrest Plaza</p>
      <p class="store-address">1450 Larkspur Ave, Millbrook,<br>OR 97410, United States</p>
      <p class="store-phone">+1 541-555-0192</p>
    </div>
  </section>

  <section class="postcard postcard--back">
    <div class="coupon-panel">
      <div class="coupon coupon--bogo">
        <span class="coupon__headline">Buy One Get One Free</span>
        <span class="coupon__condition">(Equal or Lesser Value)</span>
      </div>
      <div class="coupon coupon--save">
        <span class="coupon__save-word">Save</span>
        <span class="coupon__amount">$1</span>
      </div>
      <div class="coupon coupon--cone">
        <span class="coupon__headline">Free Waffle Cone</span>
        <span class="coupon__condition">With Froyo Purchase</span>
      </div>
      <div class="coupon coupon--smoothie">
        <span class="coupon__amount">50%</span>
        <span class="coupon__stack">Off<br>Smoothie</span>
      </div>

      <svg class="scissors" style="left:284px; top:24px"><use href="#icon-scissors"/></svg>
      <svg class="scissors" style="left:110px; top:226px"><use href="#icon-scissors"/></svg>
      <svg class="scissors" style="left:279px; top:240px"><use href="#icon-scissors"/></svg>
      <svg class="scissors" style="left:112px; top:451px"><use href="#icon-scissors"/></svg>
    </div>

    <div class="stamp-box"></div>
    <div class="address-line" style="top:193px"></div>
    <div class="address-line" style="top:217px"></div>
    <div class="address-line" style="top:242px"></div>
    <div class="address-line" style="top:267px"></div>

    <div class="back-brand"><span class="dot"></span>Tavimelon</div>
  </section>
</body>
</html>
```